We sell companies excess stock for them

We need a business card for a company based in New Zealand called 'StockHarbor'.

Check out our website to get an idea www.stockharbor.example

We help other businesses to;
- Sell Excess Stock
- Manage Product Returns
- Sell Company Assets

Our logo is attached for your reference
The font used is 'RifficFree-Bold'

Target Market(s)

Businesses

Industry/Entity Type

Business

Contact Information for Business Card

Name: Mark Pellow
Phone: 027 846 2093
email: markpellow@stockharbor.example
website: www.stockharbor.example

Font styles to use
Other font styles liked:
• Unsure

Colors
9bcb3b

Requirements
Must have
• coming soon
Nice to have
• coming soon
Should not have
• coming soon

```html
<!DOCTYPE html>
<html lang="en">
<head>
<meta charset="utf-8">
<title>StockHarbor Business Card</title>
<link rel="stylesheet" href="https://fonts.googleapis.com/css2?family=Fredoka:wght@600&family=Nunito:wght@400;600&family=PT+Serif:wght@700&display=swap">
<style>
  :root {
    --bg: #e2e2e2;
    --card-white: #ffffff;
    --forest: #365e3b;
    --ink: #1c2414;
    --text: #1a1a1a;
    --art-a: #7fb069;
    --art-b: #d9985a;
  }
  html, body {
    margin: 0;
    padding: 0;
    width: 1200px;
    height: 800px;
    overflow: hidden;
    background: var(--bg);
  }
  .stage {
    position: relative;
    width: 1200px;
    height: 800px;
  }
  .card {
    position: absolute;
    top: 247px;
    width: 542px;
    height: 305px;
    background: var(--card-white);
    overflow: hidden;
    box-shadow: 0 2px 6px rgba(0,0,0,0.18);
  }
  .card--front { left: 28px; }
  .card--back { left: 630px; }
  .card__shape {
    position: absolute;
    inset: 0;
    width: 100%;
    height: 100%;
  }
  .brand-name {
    position: absolute;
    left: 126px;
    top: 58px;
    margin: 0;
    font-family: "Fredoka", sans-serif;
    font-weight: 600;
    font-size: 30px;
    letter-spacing: -0.5px;
    color: var(--ink);
    line-height: 1;
  }
  .person-name {
    position: absolute;
    left: 175px;
    top: 94px;
    margin: 0;
    font-family: "Nunito", sans-serif;
    font-weight: 600;
    font-size: 21px;
    color: var(--text);
    line-height: 1;
  }
  .services {
    position: absolute;
    left: 165px;
    top: 131px;
    margin: 0;
    padding: 0;
    list-style: none;
    font-family: "Nunito", sans-serif;
    font-size: 13.5px;
    line-height: 18px;
    color: var(--text);
  }
  .services li::before { content: "- "; }
  .mascot-art {
    position: absolute;
    left: 325px;
    top: 76px;
    width: 150px;
    height: 150px;
    border-radius: 50%;
    background: linear-gradient(135deg, var(--art-a), var(--art-b));
  }
  .phone {
    position: absolute;
    left: 308px;
    top: 239px;
    margin: 0;
    font-family: "PT Serif", serif;
    font-weight: 700;
    font-size: 16px;
    color: var(--text);
  }
  .mascot-art--small {
    left: 418px;
    top: 45px;
    width: 64px;
    height: 64px;
  }
  .contact-lines {
    position: absolute;
    left: 130px;
    top: 118px;
    width: 370px;
    margin: 0;
    text-align: center;
    font-family: "PT Serif", serif;
    font-weight: 700;
    font-size: 16.5px;
    line-height: 22px;
    color: var(--text);
  }
</style>
</head>
<body>
<main class="stage">
  <section class="card card--front">
    <svg class="card__shape" viewBox="0 0 542 305" preserveAspectRatio="none" aria-hidden="true">
      <rect width="542" height="305" fill="var(--forest)"/>
      <path d="M119,0 H542 V305 H399 C260,282 118,225 106,130 C100,80 106,35 119,0 Z" fill="var(--card-white)"/>
    </svg>
    <h1 class="brand-name">StockHarbor</h1>
    <p class="person-name">Mark Pellow</p>
    <ul class="services">
      <li>Sell Excess Stock</li>
      <li>Manage Product Returns</li>
      <li>Sell Company Assets</li>
    </ul>
    <div class="mascot-art" role="img" aria-label="Illustration of a courier mascot carrying a parcel"></div>
    <p class="phone">tell. 027 846 2093</p>
  </section>

  <section class="card card--back">
    <svg class="card__shape" viewBox="0 0 542 305" preserveAspectRatio="none" aria-hidden="true">
      <rect width="542" height="305" fill="var(--forest)"/>
      <path d="M118,0 H542 V305 H393 C255,282 112,222 105,128 C101,78 106,33 118,0 Z" fill="var(--card-white)"/>
    </svg>
    <div class="mascot-art mascot-art--small" role="img" aria-label="Small illustration of the courier mascot"></div>
    <p class="contact-lines">
      website: www.stockharbor.example<br>
      email: markpellow@stockharbor.example
    </p>
  </section>
</main>
</body>
</html>
```